Digital Marketing Agency Needs a Pagecraft Web Design

We need a web design for a new company based in Pinecrest Hollow, Colorado (the greater Denver Metro area) called "Copper Wayfarer". We are a full service Digital Marketing Agency that offers and provides the following services to clients: Website Design, Search Engine Optimization, Plexo Local Listing, Local Online Directories, Reputation Marketing, Social Media Marketing, Video Marketing, Pay Per Click. Our slogan is "Digital Marketing, Elevated!" We want a PageCraft web design that has a very modern look. We would like to see designs use the following colors (included color code):

light blue (#0cb9ea)
orange (#f47528)
white (#ffffff)
black (#000000).

These colors coincide with the colors of our logo (attached). We prefer a flat design but would like some elements of depth. We need a header that includes a logo (attached), name/address/phone number of our company, a contact call-to-action button (these need to be very easy to locate on the page), menu bar, and banner (very flexible to set up of banner).. The footer needs to include logo, NAP, Footer Menu, Section for blogs (includes title of blog that links to post), & copyright. We also need a way to prominently display and link our key featured services (Website Design, Search Engine Optimization, Plexo Local Listing, Local Online Directories, Reputation Marketing, Social Media Marketing, Video Marketing, Pay Per Click).

Here are three websites that we really like and would like to see certain elements incorporated:

1. http://quillstonemedia.example/ (like how the services were laid out on the home page for services -- "Features" section... want to follow this same type of idea, just in our own way).
2. http://tavenmark.example/ (love the modern, visual aspect of this site and how professionally clean it is.... very easy to understand and navigate through).
3. http://norvacreative.example/ (like how this site incorporates interactive features that engage people while visiting the site).

The overall goal of the site is to effectively emphasize the services we provide (see above), who we are, and how to contact us for services.

** Any stock photos used HAVE TO BE TAKEN from Lumafold Pictures (http://www.lumafoldpics.example/). And if watermarked, please provide the image code for each image used.

Target Market(s)

Lawyers, Insurance agents, Real Estate, Restaurant Owners, Doctors and all other medical providers.

Industry/Entity Type

Internet

Number of Pages Required

1 page

Font styles to use
Serif

Colors
33a6d7
ffffff
000000
f37122

Requirements
Must have
• 1. Header w/ Logo, Name/Address/Phone Number of our business, a call-to-action button to "Contact us":
• Copper Wayfarer – Digital Marketing
• 41872 Cobblewick Drive
• Pinecrest Hollow, CO 80571
• 303-547-9183
• 2. Navigation Menu
• 3. Some type of banner
• 4. Featured Services section (with a short blurb about each)
• 5. Contact Form (somewhere above the fold)
• 6. Need at least 2-3 paragraphs of text (use dummy text) somewhere on the page (either in full or in sections)....
• 7. Footer that includes logo, NAP (see above), Menu Links, Links for services (see above), Blog Section, Social Media icons (Chatterly, Peepline, Plexo+, and ReelHub) & a copyright.
Nice to have
• Here are three websites that we really like and would be nice to see elements of incorporated:
• 1. http://quillstonemedia.example/ (like how the services were laid out on the home page -- "Features" section... want to follow this same type of idea, just in our own way).
• 2. http://tavenmark.example/ (love the modern, visual aspect of this site and how professionally clean it is.... very easy to understand and navigate through).
• 3. http://norvacreative.example/ (like how this site incorporates interactive features that engage people that visit the site).
Should not have
• Pretty flexible... We just need to make sure it's a Pagecraft web design.

```html
<!DOCTYPE html>
<html lang="en">
<head>
<meta charset="utf-8">
<title>Copper Wayfarer – Digital Marketing, Elevated!</title>
<link rel="stylesheet" href="https://fonts.googleapis.com/css2?family=Raleway:wght@400;600;700;800&family=Open+Sans:wght@400;600&display=swap">
<style>
:root{
  --blue:#0cb9ea;
  --blue-deep:#1b9fd0;
  --orange:#f47528;
  --ink:#111111;
  --dark:#1c1c1c;
  --dark-2:#2a2a2a;
  --grey:#f4f4f4;
  --text:#555555;
  --white:#ffffff;
}
*{box-sizing:border-box;margin:0;padding:0}
html,body{width:1200px;height:2588px;overflow:hidden}
body{font-family:"Open Sans",Arial,sans-serif;color:var(--text);background:var(--white);font-size:14px;line-height:1.6}
.wrap{width:1020px;margin:0 auto;position:relative;height:100%}
h1,h2,h3,h4{font-family:"Raleway",Arial,sans-serif}

/* top bar */
.top-bar{height:32px;background:var(--dark);color:#ddd;font-size:13px}
.top-bar .wrap{display:flex;align-items:center;justify-content:space-between}
.top-cta{background:var(--orange);color:var(--white);font-weight:600;height:32px;padding:0 22px;display:flex;align-items:center;gap:8px}

/* header */
.site-header{height:108px}
.site-header .wrap{display:flex;align-items:center;justify-content:space-between}
.brand{display:flex;align-items:center;gap:12px}
.brand-mark{width:46px;height:46px;border-radius:50%;background:var(--orange);flex:none}
.brand-name{font-family:"Raleway",sans-serif;font-weight:800;font-size:34px;color:var(--blue);line-height:1;white-space:nowrap}
.brand-tag{font-size:12px;color:#777;margin-top:4px;letter-spacing:.5px}
.nap{margin-left:auto;margin-right:60px;font-size:14px;color:#444;white-space:nowrap}
.nap strong{display:block;color:var(--blue);font-family:"Raleway",sans-serif;font-size:16px}
.phone{display:flex;align-items:center;gap:8px;font-weight:600;color:#333;font-size:16px;white-space:nowrap}

/* nav */
.main-nav{height:28px}
.main-nav ul{list-style:none;display:flex;background:var(--dark);height:28px;align-items:center;padding-left:30px;gap:58px}
.main-nav a{color:var(--white);text-decoration:none;font-size:13px}

/* banner */
.banner{height:340px;background:linear-gradient(180deg,#4ed0f2,var(--blue) 60%,#0aa9d8);padding-top:22px}
.banner .wrap{display:flex;height:296px;background:var(--white)}
.banner-visual{width:480px;height:296px;background:linear-gradient(135deg,#dfe8ee,#9ec9dc 50%,#f3c9a6)}
.banner-copy{flex:1;text-align:center;padding-top:40px}
.banner-copy .kicker{font-family:"Raleway",sans-serif;font-weight:800;color:var(--blue);font-size:40px;letter-spacing:1px;line-height:1.1}
.banner-copy .slogan{font-family:"Raleway",sans-serif;font-weight:800;color:var(--orange);font-size:64px;line-height:1.1}
.banner-copy .sub{font-family:"Raleway",sans-serif;font-weight:700;color:#333;font-size:20px;line-height:1.3;margin-top:10px}
.btn{display:inline-block;background:var(--orange);color:var(--white);font-weight:600;font-size:12px;padding:8px 20px;text-decoration:none}
.banner-copy .btn{margin-top:18px}

/* welcome */
.welcome{height:320px;padding-top:40px}
.welcome .wrap{display:flex;gap:50px}
.welcome-text{flex:1}
.welcome h1{font-size:32px;color:var(--blue);font-weight:700;margin-bottom:16px}
.welcome h1 span{color:var(--orange)}
.welcome p{font-size:13px;margin-bottom:14px}
.welcome-visual{width:420px;height:170px;background:linear-gradient(135deg,#f2c7a0,#7bc3df 50%,#e9eef1);margin-top:6px}

/* services */
.services{height:940px;background:var(--grey);padding-top:40px}
.section-title{text-align:center;font-size:30px;color:var(--blue);font-weight:700;position:relative}
.section-title::after{content:"";display:block;width:280px;height:2px;background:var(--blue);margin:6px auto 0}
.services-intro{text-align:center;font-size:13px;margin:18px 60px 36px}
.service-grid{display:grid;grid-template-columns:1fr 1fr;column-gap:60px;row-gap:46px}
.service{display:flex;gap:18px;height:140px}
.service-visual{width:120px;height:120px;flex:none;border-radius:6px}
.service h3{color:var(--orange);font-size:18px;font-weight:700;margin-bottom:4px}
.service p{font-size:12px;line-height:1.55;margin-bottom:8px}
.more{display:inline-flex;align-items:center;gap:6px;background:var(--dark);color:var(--white);font-size:11px;padding:3px 10px 3px 4px;text-decoration:none}
.more i{width:14px;height:14px;background:var(--blue);display:inline-block}

/* contact */
.contact{height:420px;background:var(--white);padding-top:20px}
.contact .wrap{background:var(--dark);height:380px;padding:0 40px}
.contact-tab{position:absolute;left:50%;transform:translateX(-50%);top:-14px;background:var(--blue);color:var(--white);font-family:"Raleway",sans-serif;font-weight:700;font-size:20px;padding:10px 36px}
.contact-form{padding-top:90px}
.field-row{display:flex;gap:20px;margin-bottom:20px}
.field{flex:1;height:40px;border:1px solid #555;background:var(--dark-2);color:#999;font-size:12px;padding:10px 12px}
.field.area{height:110px}
.send{display:block;width:100%;background:var(--orange);color:var(--white);text-align:center;font-weight:600;padding:10px 0;font-size:14px}

/* footer */
.site-footer{height:428px;background:var(--blue);color:var(--white);padding-top:40px}
.footer-cols{display:grid;grid-template-columns:1.3fr 1fr 1fr 1fr;gap:40px}
.site-footer h4{font-size:18px;font-weight:700;margin-bottom:22px}
.footer-brand{background:var(--white);display:flex;align-items:center;gap:8px;padding:12px 14px;width:230px;margin-bottom:14px}
.footer-brand .brand-mark{width:26px;height:26px}
.footer-brand span{font-family:"Raleway",sans-serif;font-weight:800;color:var(--blue);font-size:19px;white-space:nowrap;line-height:1}
.site-footer p,.site-footer li{font-size:12px;line-height:1.9}
.site-footer ul{list-style:none}
.site-footer li::before{content:"› ";}
.blog-post{display:flex;gap:10px;margin-bottom:14px}
.blog-thumb{width:56px;height:44px;flex:none;background:linear-gradient(135deg,#e8eef2,#8fb8c9)}
.blog-post a{color:var(--white);text-decoration:none;font-size:12px;line-height:1.4}
.footer-bottom{position:absolute;left:0;right:0;top:318px;display:flex;justify-content:space-between;align-items:center;font-size:12px}
.social{display:flex;gap:8px}
.social span{width:34px;height:34px;background:var(--dark)}
</style>
</head>
<body>

<div class="top-bar"><div class="wrap">
  <span>Welcome to Copper Wayfarer</span>
  <a class="top-cta"><svg width="14" height="14" viewBox="0 0 24 24"><path fill="#fff" d="M2 5h20v14H2z M2 5l10 8 10-8" stroke="#f47528" stroke-width="1.5"/></svg>Contact Us</a>
</div></div>

<header class="site-header"><div class="wrap">
  <div>
    <div class="brand"><span class="brand-mark"></span><span class="brand-name">Copper Wayfarer</span></div>
    <div class="brand-tag">Digital Marketing, Elevated!</div>
  </div>
  <div class="nap"><strong>Copper Wayfarer – Digital Marketing</strong>41872 Cobblewick Drive | Pinecrest Hollow, CO 80571</div>
  <div class="phone"><svg width="18" height="18" viewBox="0 0 24 24"><path fill="#f47528" d="M6.6 10.8a15 15 0 0 0 6.6 6.6l2.2-2.2a1 1 0 0 1 1-.25 11.4 11.4 0 0 0 3.6.57 1 1 0 0 1 1 1V20a1 1 0 0 1-1 1A17 17 0 0 1 3 4a1 1 0 0 1 1-1h3.5a1 1 0 0 1 1 1c0 1.25.2 2.45.57 3.57a1 1 0 0 1-.25 1z"/></svg>303-547-9183</div>
</div></header>

<nav class="main-nav"><div class="wrap"><ul>
  <li><a>Home</a></li><li><a>About Us</a></li><li><a>Services</a></li><li><a>Blog</a></li><li><a>Contact Us</a></li>
</ul></div></nav>

<section class="banner"><div class="wrap">
  <div class="banner-visual" role="img" aria-label="Collage of digital marketing concepts with hands and innovation keywords"></div>
  <div class="banner-copy">
    <div class="kicker">DIGITAL MARKETING</div>
    <div class="slogan">ELEVATED!</div>
    <div class="sub">SED UT PERSPICIATIS UNDE OMNIS<br>DOLOR SIT AMET, CONSECTETUR</div>
    <a class="btn">READ MORE</a>
  </div>
</div></section>

<section class="welcome"><div class="wrap">
  <div class="welcome-text">
    <h1>Welcome to <span>Copper Wayfarer</span></h1>
    <p>The standard chunk of Lorem Ipsum used since the 1500s is reproduced below for those interested. Sections 1.10.32 and 1.10.33 from "de Finibus Bonorum et Malorum" by Cicero are also reproduced in their exact original form, accompanied by English versions from the 1914 translation by H. Rackham.</p>
    <p>Lorem Ipsum is simply dummy text of the printing and typesetting industry. Lorem Ipsum has been the industry's standard dummy text ever since the 1500s, when an unknown printer took a galley of type.</p>
  </div>
  <div class="welcome-visual" role="img" aria-label="Digital marketing strategy illustration with icons and charts"></div>
</div></section>

<section class="services"><div class="wrap">
  <h2 class="section-title">Featured Services</h2>
  <p class="services-intro">Lorem Ipsum is simply dummy text of the printing and typesetting industry. Lorem Ipsum has been the industry's standard dummy text ever since the 1500s, when an unknown printer took a galley of type and scrambled it to make a type specimen book. It has survived not only five centuries, but also the leap into electronic typesetting, remaining essentially unchanged.</p>
  <div class="service-grid">
    <article class="service"><div class="service-visual" style="background:linear-gradient(135deg,#d9a77a,#6f8ea0)" role="img" aria-label="Hands working on a laptop for website design"></div><div><h3>Website Design</h3><p>Lorem Ipsum is simply dummy text of the printing and typesetting industry. Lorem Ipsum has been the industry's standard dummy text ever since the 1500s, when an unknown printer took a galley of type and scrambled it.</p><a class="more"><i></i>Read More</a></div></article>
    <article class="service"><div class="service-visual" style="background:linear-gradient(135deg,#0b3f8a,#2f86d6)" role="img" aria-label="Blue search concept graphic"></div><div><h3>Search Engine Optimization</h3><p>Lorem Ipsum is simply dummy text of the printing and typesetting industry. Lorem Ipsum has been the industry's standard dummy text ever since the 1500s, when an unknown printer took a galley of type and scrambled it.</p><a class="more"><i></i>Read More</a></div></article>
    <article class="service"><div class="service-visual" style="background:linear-gradient(135deg,#c9d8e2,#4e7d9a)" role="img" aria-label="Business listing on a map"></div><div><h3>Plexo Local Listing</h3><p>Lorem Ipsum is simply dummy text of the printing and typesetting industry. Lorem Ipsum has been the industry's standard dummy text ever since the 1500s, when an unknown printer took a galley of type and scrambled it.</p><a class="more"><i></i>Read More</a></div></article>
    <article class="service"><div class="service-visual" style="background:linear-gradient(135deg,#e4e9ee,#8da9c4)" role="img" aria-label="Network of connected directory nodes"></div><div><h3>Local Online Directories</h3><p>Lorem Ipsum is simply dummy text of the printing and typesetting industry. Lorem Ipsum has been the industry's standard dummy text ever since the 1500s, when an unknown printer took a galley of type and scrambled it.</p><a class="more"><i></i>Read More</a></div></article>
    <article class="service"><div class="service-visual" style="background:linear-gradient(135deg,#5d6f7c,#c7b69a)" role="img" aria-label="Reputation rating concept"></div><div><h3>Reputation Marketing</h3><p>Lorem Ipsum is simply dummy text of the printing and typesetting industry. Lorem Ipsum has been the industry's standard dummy text ever since the 1500s, when an unknown printer took a galley of type and scrambled it.</p><a class="more"><i></i>Read More</a></div></article>
    <article class="service"><div class="service-visual" style="background:linear-gradient(135deg,#f0f0f0,#9fb3c2)" role="img" aria-label="Social media network concept"></div><div><h3>Social Media Marketing</h3><p>Lorem Ipsum is simply dummy text of the printing and typesetting industry. Lorem Ipsum has been the industry's standard dummy text ever since the 1500s, when an unknown printer took a galley of type and scrambled it.</p><a class="more"><i></i>Read More</a></div></article>
    <article class="service"><div class="service-visual" style="background:linear-gradient(135deg,#2d5b86,#a9c7e0)" role="img" aria-label="Video player on a tablet"></div><div><h3>Video Marketing</h3><p>Lorem Ipsum is simply dummy text of the printing and typesetting industry. Lorem Ipsum has been the industry's standard dummy text ever since the 1500s, when an unknown printer took a galley of type and scrambled it.</p><a class="more"><i></i>Read More</a></div></article>
    <article class="service"><div class="service-visual" style="background:linear-gradient(135deg,#e8e8e8,#9a9a9a)" role="img" aria-label="Pay per click keyboard concept"></div><div><h3>Pay Per Click</h3><p>Lorem Ipsum is simply dummy text of the printing and typesetting industry. Lorem Ipsum has been the industry's standard dummy text ever since the 1500s, when an unknown printer took a galley of type and scrambled it.</p><a class="more"><i></i>Read More</a></div></article>
  </div>
</div></section>

<section class="contact"><div class="wrap">
  <div class="contact-tab">Contact Us</div>
  <form class="contact-form">
    <div class="field-row"><div class="field">Your Name</div><div class="field">Your Email</div><div class="field">Your Phone</div></div>
    <div class="field-row"><div class="field area">Your Message</div></div>
    <div class="send">Send</div>
  </form>
</div></section>

<footer class="site-footer"><div class="wrap">
  <div class="footer-cols">
    <div>
      <h4>Copper Wayfarer</h4>
      <div class="footer-brand"><span class="brand-mark"></span><span>Copper Wayfarer</span></div>
      <p>41872 Cobblewick Drive<br>Pinecrest Hollow, CO 80571<br>303-547-9183</p>
    </div>
    <div>
      <h4>Site Map</h4>
      <ul><li>Home</li><li>About Us</li><li>Services</li><li>Blog</li><li>Contact Us</li></ul>
    </div>
    <div>
      <h4>Services</h4>
      <ul><li>Website Design</li><li>SEO</li><li>Plexo Local Listing</li><li>Local Online Directories</li><li>Reputation Marketing</li><li>Social Media Marketing</li><li>Video Marketing</li><li>Pay Per Click</li></ul>
    </div>
    <div>
      <h4>Blog</h4>
      <div class="blog-post"><div class="blog-thumb" role="img" aria-label="Blog post thumbnail"></div><a>Lorem ipsum dolor sit amet consectetur elit</a></div>
      <div class="blog-post"><div class="blog-thumb" role="img" aria-label="Blog post thumbnail"></div><a>Sed ut perspiciatis unde omnis iste natus</a></div>
      <div class="blog-post"><div class="blog-thumb" role="img" aria-label="Blog post thumbnail"></div><a>Nemo enim ipsam voluptatem quia voluptas</a></div>
    </div>
  </div>
  <div class="footer-bottom">
    <span>© Copper Wayfarer. All Rights Reserved.</span>
    <div class="social" aria-label="Chatterly, Peepline, Plexo+, ReelHub"><span></span><span></span><span></span><span></span></div>
  </div>
</div></footer>

</body>
</html>
```